Road Construction Company needs business cards

We would like a new business card designed for our business.

We're a road construction company based in Qld, Australia.

Can the business card please have the following information on it.

Name: Brent Malvoy
Position: General Manager
Phone: 0471 592 304
Email: Brent.malvoy@quendix.com.au
Address: 87 Harrowgate Ave, Pindarra, QLD, 4000
Website: www.quendix.com.au

Visually we'd like the card to be professional and simple.

Attached is our logo.

Our website is www.quendix.com.au

Target Market(s)

Men aged 25-60

Contact Information for Business Card

As listed in project description

Font styles to use
Serif

Requirements
Must have
• Large logo on back of card

```html
<!DOCTYPE html>
<html lang="en">
<head>
<meta charset="utf-8">
<title>Quendix Business Card</title>
<link href="https://fonts.googleapis.com/css2?family=Source+Serif+4:opsz,wght@8..60,400;8..60,700&display=swap" rel="stylesheet">
<style>
  :root {
    --brand-blue: #0a3ef5;
    --brand-cyan: #4ccff5;
    --paper: #ffffff;
    --backdrop: #ffffff;
  }
  * { margin: 0; padding: 0; box-sizing: border-box; }
  html, body {
    width: 996px; height: 1200px; overflow: hidden;
    background: var(--backdrop);
    font-family: "Source Serif 4", Georgia, serif;
  }
  .canvas { position: relative; width: 996px; height: 1200px; }
  .card {
    position: absolute; left: 48px; width: 900px; height: 499px;
    box-shadow: 0 8px 24px rgba(0,0,0,0.28);
    overflow: hidden;
  }
  .card-front { top: 88px; background: var(--brand-blue); }
  .card-back { top: 631px; background: var(--paper); }

  .stripes { position: absolute; inset: 0; width: 900px; height: 499px; }

  .holder-name {
    position: absolute; left: 92px; top: 76px;
    font-size: 55px; font-weight: 700; color: var(--paper);
    line-height: 1; letter-spacing: -0.3px;
  }
  .holder-role {
    position: absolute; left: 92px; top: 150px;
    font-size: 36px; font-weight: 400; color: var(--brand-cyan); line-height: 1;
  }
  .contact-list {
    position: absolute; left: 92px; top: 272px; list-style: none;
  }
  .contact-item {
    display: flex; align-items: center; height: 42px;
    font-size: 25px; color: var(--paper);
  }
  .contact-icon {
    width: 28px; height: 28px; margin-right: 13px; flex: none;
    fill: none; stroke: var(--brand-cyan); stroke-width: 1.6;
    stroke-linecap: round; stroke-linejoin: round;
  }

  .brand-name {
    position: absolute; left: 0; right: 0; top: 150px;
    text-align: center; font-size: 118px; font-weight: 700;
    color: var(--brand-blue); line-height: 1; letter-spacing: 4px;
  }
  .back-web {
    position: absolute; left: 0; right: 0; top: 411px;
    text-align: center; font-size: 26px; color: var(--brand-cyan);
  }
</style>
</head>
<body>
<div class="canvas">
  <section class="card card-front">
    <svg class="stripes" viewBox="0 0 900 499" aria-hidden="true">
      <polygon points="795,134 900,134 900,281 794,499 611,499" fill="#ffffff"/>
      <polygon points="900,356 900,499 832,499" fill="var(--brand-cyan)"/>
    </svg>
    <h1 class="holder-name">Brent Malvoy</h1>
    <p class="holder-role">General Manager</p>
    <ul class="contact-list">
      <li class="contact-item">
        <svg class="contact-icon" viewBox="0 0 24 24" aria-hidden="true"><path d="M5 3h4l2 5-2.5 1.5a11 11 0 0 0 6 6L16 13l5 2v4a2 2 0 0 1-2 2A16 16 0 0 1 3 5a2 2 0 0 1 2-2z"/></svg>
        0471 592 304
      </li>
      <li class="contact-item">
        <svg class="contact-icon" viewBox="0 0 24 24" aria-hidden="true"><rect x="3" y="8" width="18" height="13"/><path d="M3 8l9 7 9-7M7 8V3h10v5"/><circle cx="12" cy="7" r="2"/></svg>
        Brent.malvoy@quendix.com.au
      </li>
      <li class="contact-item">
        <svg class="contact-icon" viewBox="0 0 24 24" aria-hidden="true"><path d="M2 12L12 3l10 9M5 10v11h14V10M10 21v-6h4v6"/></svg>
        87 Harrowgate Ave, Pindarra, QLD, 4000
      </li>
      <li class="contact-item">
        <svg class="contact-icon" viewBox="0 0 24 24" aria-hidden="true"><circle cx="12" cy="12" r="9"/><ellipse cx="12" cy="12" rx="4" ry="9"/><path d="M3 12h18M4.5 7.5h15M4.5 16.5h15"/></svg>
        www.quendix.com.au
      </li>
    </ul>
  </section>

  <section class="card card-back">
    <p class="brand-name">QUENDIX</p>
    <p class="back-web">www.quendix.com.au</p>
  </section>
</div>
</body>
</html>
```